Locksmith Store 474747 Signage

Design Brief: Locksmith Store Signage – "Locksmith 474747" [ΚΛΕΙΔΑΡΑΣ 474747 (in Greek)]
We are looking for a spectacular and professional sign design for the exterior of our locksmith store.
Signage Dimensions:
• Width: 6 meters
• Height: 1.5 meters
• Shopfront window Width: 6 meters, Height: 2.5 meters
Key Requirements (in order of importance):
1. It must be immediately clear that this is a locksmith store. [ΚΛΕΙΔΑΡΑΣ (in Greek)]
2. The store name "474747", (which is also the phone number 2310474747), should be highly visible and visually striking because this is the number that customers are calling when they are locked out.
3. The signage should also clearly communicate that except for house keys, which is obvious for a locksmith store the services we provide are:
o All kinds of house keys. ΚΛΕΙΔΙΑ ΣΠΙΤΙΩΝ(in Greek) (There is no key that we cannot do)
o Immobiliser car keys = ΚΛΕΙΔΙΑ ΑΥΤΟΚΙΝΗΤΩΝ (in Greek)
We unlock every car that exist, we program new immobilizer keys – remote controls, even if all keys are lost, we repair or change broken cells of car keys, we change batteries.
o High-security locks = ΚΛΕΙΔΑΡΙΕΣ ΑΣΦΑΛΕΙΑΣ (in Greek) we sell the best high security locks in the planet
o Armoured doors = ΠΟΡΤΕΣ ΑΣΦΑΛΕΙΑΣ (in Greek) (this may not be so important to be on the signage.
Visual Style:
We are open to creative direction, but the design should be eye-catching, professional, and modern, something that will stand out on a busy street and instantly tell customers who we are and what we offer. Also, you may use the shopfront window for graphic designs. Also, we are open if a part of the signage is digital.
________________________________________
Updates
Hello Designers,
Thank you so much for your effort and the designs you've shared.
I realized I forgot to mention that you can refer to my website at www.474747-keys.example.gr for more context.
Additionally, I’ve just uploaded two new photos: one showing the store with a black outline at the dimensions of the signage, and another with the large double-bit key placed in a different position to demonstrate that it is moveable.
Thanks again for your dedication!
Target Market(s)
every person that has a key
Look and feel
Each slider illustrates characteristics of the customer's brand and the style your logo design should communicate.

```html
<!DOCTYPE html>
<html lang="el">
<head>
<meta charset="UTF-8">
<title>ΚΛΕΙΔΑΡΑΣ 474747 – Πινακίδα καταστήματος</title>
<link rel="stylesheet" href="https://fonts.googleapis.com/css2?family=Noto+Sans:ital,wght@0,700;0,900;1,800&display=swap">
<style>
  :root {
    --page-bg: #ececec;
    --sign-yellow: #e6bd2e;
    --sign-yellow-edge: #dea33d;
    --ink: #161616;
    --band: #1b1b1b;
    --white: #f5f5f5;
    --gold-light: #f4d489;
    --gold-mid: #c9962f;
    --gold-dark: #7d5512;
  }
  * { margin: 0; padding: 0; box-sizing: border-box; }
  html, body {
    width: 1181px;
    height: 1200px;
    overflow: hidden;
    background: var(--page-bg);
  }
  .canvas {
    position: relative;
    width: 1181px;
    height: 1200px;
  }
  .sign {
    position: absolute;
    left: 40px;
    top: 462px;
    width: 1101px;
    height: 275px;
    overflow: hidden;
    background:
      radial-gradient(ellipse 60% 90% at 45% 45%, #e8c22c 0%, rgba(232,194,44,0) 100%),
      linear-gradient(90deg, var(--sign-yellow-edge), var(--sign-yellow) 20%, var(--sign-yellow) 75%, var(--sign-yellow-edge));
    font-family: "Noto Sans", sans-serif;
  }
  .trade-name {
    position: absolute;
    left: 106px;
    top: 14px;
    font-size: 86px;
    font-weight: 900;
    line-height: 1;
    color: var(--ink);
    letter-spacing: 1px;
    transform: scaleX(1.22);
    transform-origin: left top;
    white-space: nowrap;
  }
  .store-number {
    position: absolute;
    top: 104px;
    font-size: 132px;
    font-weight: 900;
    line-height: 1;
    color: var(--white);
    text-shadow: 0 4px 6px rgba(120, 80, 0, 0.35);
    transform: scaleX(1.18);
    transform-origin: left top;
    letter-spacing: -2px;
    white-space: nowrap;
  }
  .store-number--first { left: 128px; }
  .store-number--second { left: 478px; }
  .padlock {
    position: absolute;
    left: 373px;
    top: 70px;
    width: 106px;
    height: 139px;
    border-radius: 10px 10px 6px 6px;
    background: linear-gradient(135deg, var(--gold-light), var(--gold-mid) 55%, var(--gold-dark));
    box-shadow: 0 4px 8px rgba(90, 60, 0, 0.4);
  }
  .contact {
    position: absolute;
    top: 236px;
    display: flex;
    align-items: center;
    gap: 14px;
    color: var(--ink);
    font-weight: 900;
    white-space: nowrap;
  }
  .contact--phone { left: 130px; top: 229px; font-size: 29px; letter-spacing: 0.5px; }
  .contact--web { left: 488px; top: 233px; font-size: 19px; }
  .contact svg { flex: none; }
  .services {
    position: absolute;
    right: 0;
    top: 24px;
    width: 280px;
    height: 226px;
  }
  .service {
    position: absolute;
    right: 0;
    height: 63px;
    background: var(--band);
    clip-path: polygon(12px 0, 100% 0, 100% 100%, 0 100%);
    display: flex;
    align-items: center;
    gap: 14px;
    padding-left: 30px;
    color: var(--white);
  }
  .service--doors { top: 0; width: 240px; padding-left: 30px; }
  .service--locks { top: 82px; width: 257px; }
  .service--keys { top: 163px; width: 273px; }
  .service-label {
    font-style: italic;
    font-weight: 800;
    font-size: 19px;
    line-height: 0.98;
    text-align: center;
    letter-spacing: 0.3px;
  }
</style>
</head>
<body>
<main class="canvas">
  <section class="sign" aria-label="Πινακίδα καταστήματος ΚΛΕΙΔΑΡΑΣ 474747">
    <h1 class="trade-name">ΚΛΕΙΔΑΡΑΣ</h1>
    <div class="store-number store-number--first">474</div>
    <div class="store-number store-number--second">747</div>
    <div class="padlock" role="img" aria-label="Χρυσό λουκέτο με κλειδαρότρυπα"></div>

    <div class="contact contact--phone">
      <svg width="38" height="38" viewBox="0 0 24 24" aria-hidden="true">
        <path fill="#161616" d="M6.6 10.8a15.1 15.1 0 0 0 6.6 6.6l2.2-2.2a1 1 0 0 1 1-.25 11.4 11.4 0 0 0 3.6.57 1 1 0 0 1 1 1V20a1 1 0 0 1-1 1A17 17 0 0 1 3 4a1 1 0 0 1 1-1h3.5a1 1 0 0 1 1 1c0 1.25.2 2.45.57 3.57a1 1 0 0 1-.25 1z"/>
      </svg>
      <span>2310474747</span>
    </div>

    <div class="contact contact--web">
      <svg width="30" height="34" viewBox="0 0 20 24" aria-hidden="true">
        <path fill="#161616" d="M2 1l16 11-7 1.2 4.2 8.2-3 1.5-4.2-8.3L3 19z"/>
      </svg>
      <span>474747-KEYS.EXAMPLE.GR</span>
    </div>

    <div class="services">
      <div class="service service--doors">
        <svg class="key-icon" width="34" height="34" viewBox="0 0 32 32" aria-hidden="true">
          <circle cx="10" cy="22" r="8" fill="#f5f5f5"/>
          <circle cx="8" cy="24" r="2.4" fill="#1b1b1b"/>
          <path fill="#f5f5f5" d="M13 16 24 5l3 3-2 2 2 2-2 2-2-2-2 2 2 2-2 2-2-2-3 3z"/>
        </svg>
        <span class="service-label">ΠΟΡΤΕΣ<br>ΑΣΦΑΛΕΙΑΣ</span>
      </div>
      <div class="service service--locks">
        <svg class="key-icon" width="34" height="34" viewBox="0 0 32 32" aria-hidden="true">
          <circle cx="10" cy="22" r="8" fill="#f5f5f5"/>
          <circle cx="8" cy="24" r="2.4" fill="#1b1b1b"/>
          <path fill="#f5f5f5" d="M13 16 24 5l3 3-2 2 2 2-2 2-2-2-2 2 2 2-2 2-2-2-3 3z"/>
        </svg>
        <span class="service-label">ΚΛΕΙΔΑΡΙΕΣ<br>ΑΣΦΑΛΕΙΑΣ</span>
      </div>
      <div class="service service--keys">
        <svg class="key-icon" width="34" height="34" viewBox="0 0 32 32" aria-hidden="true">
          <circle cx="10" cy="22" r="8" fill="#f5f5f5"/>
          <circle cx="8" cy="24" r="2.4" fill="#1b1b1b"/>
          <path fill="#f5f5f5" d="M13 16 24 5l3 3-2 2 2 2-2 2-2-2-2 2 2 2-2 2-2-2-3 3z"/>
        </svg>
        <span class="service-label">ΚΛΕΙΔΙ ΣΠΙΤΙΟΥ<br>ΑΥΤΟΚΙΝΗΤΟΥ</span>
      </div>
    </div>
  </section>
</main>
</body>
</html>
```